Multiple website banners for a shopify theme

I need custom designed banners for a destributor webpage.

We will be selling products in our local store from a supplier https://pipwellsoaps.co.uk (you can get the ideas from their site).

We need custom desings:
- 2-3x 1920x745
- 1x 960x960
- 2x 480x480
- 1x 960*480
All of theme need to nicely fit together as shown in the uploaded layout screenshot (website_banner_layout).
In Google drive link there are products pictures which must be used in the banners.

https://files.mornavex.com/share/folders/8QpTzK2wLmVa7HnYcRbE5dUsXoGi3JfKt?usp=sharing

Target Market(s)

Kids, Cosmetics market

Industry/Entity Type

Cosmetics

Requirements
Must have
• Playful elements

```html
<!DOCTYPE html>
<html lang="en">
<head>
<meta charset="utf-8">
<title>Sale in LumiBook – Banner</title>
<link rel="stylesheet" href="https://fonts.googleapis.com/css2?family=Italiana&family=Marcellus&display=swap">
<style>
  :root{
    --blush:#f8c3c3;
    --blush-light:#fbd3d1;
    --coral:#fb6552;
    --coral-soft:#fd7a66;
    --crimson:#b50d18;
    --title-red:#9e1420;
    --ink:#2a0a0a;
    --white:#ffffff;
  }
  html,body{margin:0;padding:0;overflow:hidden;background:var(--white);}
  .banner{
    position:relative;width:1200px;height:466px;overflow:hidden;
    background:linear-gradient(100deg,var(--blush) 0%,var(--blush-light) 60%,var(--blush) 100%);
    font-family:"Italiana",serif;
  }
  .backdrop{position:absolute;inset:0;width:1200px;height:466px;}
  .model-photo{
    position:absolute;left:96px;top:18px;width:420px;height:448px;
    border-radius:200px 200px 0 0;
    background:radial-gradient(ellipse at 55% 30%,#f3c6b0 0%,#e7a896 28%,#d99fbd 55%,#c9b4e0 80%,#bfaee0 100%);
  }
  .headline{
    position:absolute;left:455px;top:22px;margin:0;
    font-family:"Italiana",serif;font-weight:400;
    color:var(--title-red);font-size:98px;line-height:78px;letter-spacing:1px;
    text-shadow:0 0 12px rgba(255,255,255,.55);
  }
  .headline span{display:block;}
  .perks{position:absolute;left:559px;top:222px;margin:0;padding:0;list-style:none;}
  .perk{display:flex;align-items:center;height:52px;}
  .perk-icon{width:43px;height:43px;border-radius:50%;background:var(--white);
    display:flex;align-items:center;justify-content:center;margin-right:13px;flex:none;}
  .perk-icon svg{width:26px;height:26px;}
  .perk-text{font-family:"Marcellus",serif;font-size:36px;color:var(--ink);letter-spacing:-.5px;white-space:nowrap;}
  .brand-badge{
    position:absolute;left:956px;top:-170px;width:340px;height:340px;border-radius:50%;
    background:var(--crimson);
  }
  .brand-name{
    position:absolute;left:1002px;top:70px;margin:0;
    font-family:"Marcellus",serif;color:var(--white);
    font-size:22px;line-height:26px;white-space:nowrap;
  }
</style>
</head>
<body>
<div class="banner">
  <svg class="backdrop" viewBox="0 0 1200 466" aria-hidden="true">
    <g fill="#ffffff" opacity=".12">
      <circle cx="620" cy="70" r="90"/>
      <polygon points="880,0 950,0 540,466 470,466"/>
      <circle cx="855" cy="360" r="110"/>
    </g>
    <path fill="var(--coral)" d="M0,168 C70,158 130,200 180,260 L300,466 L0,466 Z"/>
    <path fill="var(--coral)" d="M440,330 C560,240 700,192 860,195 C1000,198 1110,222 1200,240 L1200,466 L440,466 Z"/>
    <g fill="var(--coral-soft)" opacity=".5">
      <circle cx="855" cy="360" r="110"/>
    </g>
  </svg>

  <div class="model-photo" role="img" aria-label="Smiling woman in a red beret and lilac blouse holding an open red lip gloss and its wand"></div>

  <h1 class="headline"><span>Sale in</span><span>LumiBook</span></h1>

  <ul class="perks">
    <li class="perk">
      <span class="perk-icon"><svg viewBox="0 0 24 24"><path fill="var(--crimson)" d="M12 2l2.9 6.3 6.9.7-5.2 4.6 1.5 6.8L12 16.9 5.9 20.4l1.5-6.8L2.2 9l6.9-.7z"/></svg></span>
      <span class="perk-text">Exclusive Deals</span>
    </li>
    <li class="perk">
      <span class="perk-icon"><svg viewBox="0 0 24 24"><path fill="var(--crimson)" d="M12 2C9 7 5 10 5 15a7 7 0 0 0 14 0c0-5-4-8-7-13z"/><g stroke="#fff" stroke-width="1.6" fill="none"><line x1="9.5" y1="18" x2="14.5" y2="12"/><circle cx="9.8" cy="12.6" r="1.2"/><circle cx="14.2" cy="17.4" r="1.2"/></g></svg></span>
      <span class="perk-text">Massive Discounts</span>
    </li>
    <li class="perk">
      <span class="perk-icon"><svg viewBox="0 0 24 24"><path fill="var(--crimson)" d="M9 2h6l-1 5 2 3-1 2 5 10H4l5-10-1-2 2-3z"/></svg></span>
      <span class="perk-text">Wide Range of Products</span>
    </li>
    <li class="perk">
      <span class="perk-icon"><svg viewBox="0 0 24 24"><circle cx="8" cy="7" r="5" fill="var(--crimson)"/><text x="8" y="9.5" font-size="7" text-anchor="middle" fill="#fff" font-family="sans-serif">$</text><path fill="var(--crimson)" d="M11 13h3l1-4c1.5 0 2 1 1.8 2.5L16.5 13H21v3l-1.5 6H11z"/></svg></span>
      <span class="perk-text">Jaw Dropping Prices</span>
    </li>
  </ul>

  <div class="brand-badge"></div>
  <p class="brand-name">Fizzora Kozmetika</p>
</div>
</body>
</html>
```